Wordpress Design Project (Varnet)

We need a wordpress design for an established auction and real estate company based in Pennsylvania. The winning design will incorporate a professional layout with and company logo in a very simple and clean layout.

Industry/Entity Type

Real Estate

Requirements
Must have
• Navigation:
1) Home; 2) Auctions; 3) Appraisals; 4) Real Estate; 5) FAQ; 6) About Us; 7) Contact Us.

Site will have overall layout of https://www.plimtova.com/featured/regions/the-northeast. Home page will have logo and navigation at top. The navigation bar will also have social media icons (facebook, Google+, RSS, twitter) inside it. There will be text in the content area - use lorem ipsum. The image attached will be used below text (auctions.jpg) . Footer will have smaller company loogo, the attached affiliation logos and social media icons.

Logo attached. Color scheme will be black, gray, and red as accent color.
Nice to have
• navigation will have dropdowns, nice to have one represented - under auctions 'All Auctions' will be dropdown.

```html
<!DOCTYPE html>
<html lang="en">
<head>
<meta charset="utf-8">
<title>Varnet Auctioneers &amp; Appraisers</title>
<link href="https://fonts.googleapis.com/css2?family=Arimo:wght@400;700&display=swap" rel="stylesheet">
<style>
  :root{
    --red:#d9201c;
    --red-dark:#b8140f;
    --ink:#333;
    --muted:#888;
    --text:#777;
    --slate:#474b52;
    --band:#ececec;
    --frame:#d6d6d6;
    --white:#fff;
  }
  *{box-sizing:border-box;margin:0;padding:0}
  html,body{width:1029px;height:1200px;overflow:hidden}
  body{font-family:"Arimo",Arial,sans-serif;background:linear-gradient(#fbfbfb,#dcdcdc 88%,#e6e6e6);position:relative;color:var(--ink)}
  .page{position:absolute;left:82px;top:0;width:858px;height:1200px;background:var(--white)}
  .page > *{position:absolute}

  .brand{left:4px;top:10px;display:flex;align-items:center;gap:8px}
  .brand-mark{width:42px;height:42px;background:var(--red)}
  .brand-name{font-size:30px;font-weight:400;color:var(--ink);letter-spacing:1px}

  .social{right:20px;top:10px;display:flex;gap:2px}
  .social span{width:18px;height:18px;border-radius:50%;background:var(--red)}
  .social span:nth-child(2n){background:var(--slate)}

  .main-nav{right:10px;top:42px;display:flex;gap:25px;font-size:11.5px}
  .main-nav a{color:var(--red);text-decoration:none;padding-bottom:3px}
  .main-nav a.current{border-bottom:1px solid var(--red)}

  .hero{left:0;top:69px;width:858px;height:270px;background:linear-gradient(90deg,#7a5446 0%,#a27a68 40%,#b99684 70%,#d8c7b6 100%)}
  .hero-copy{position:absolute;left:31px;top:55px;color:var(--white);width:300px}
  .hero h1{font-size:23px;font-weight:700;line-height:28px;letter-spacing:.3px}
  .hero p{font-size:11px;line-height:15.5px;margin-top:14px}
  .hero p b{display:block}
  .dots{position:absolute;left:34px;top:234px;display:flex;gap:3px}
  .dots i{width:10px;height:7px;background:#333}

  .card{width:386px}
  .card .photo{height:180px;border:3px solid #e9e9e9;outline:1px solid var(--frame)}
  .card p{font-size:10.5px;line-height:17px;color:var(--text);padding:0 8px;margin-top:6px}
  .card p a{color:var(--red);text-decoration:none;margin-left:4px}
  .c1{left:32px;top:377px}
  .c2{left:447px;top:377px}
  .c2 p{margin-top:14px}
  .c3{left:29px;top:611px;width:384px}
  .c4{left:447px;top:611px;width:385px}

  .subscribe{left:0;top:862px;width:858px;text-align:center}
  .subscribe h2{font-size:20px;font-weight:400;color:var(--muted)}
  .subscribe p{font-size:10px;color:var(--muted);line-height:12px;margin-top:6px}
  .form{display:flex;gap:16px;justify-content:center;margin-top:20px;margin-left:-14px}
  .form .field{width:220px;height:41px;border:1px solid #ccc;font-size:11px;color:#444;text-align:left;padding:14px 15px}
  .form .btn{width:168px;height:41px;background:var(--slate);color:var(--white);font-size:18px;line-height:41px}

  .partners{left:0;top:1013px;width:858px;height:78px;background:var(--band);display:flex;align-items:center;justify-content:space-between;padding:0 28px}
  .arrow{width:17px;height:17px;border-radius:50%;background:#555;display:flex;align-items:center;justify-content:center}
  .badge{width:60px;height:46px;background:#c9c9c9}
  .badge.round{border-radius:50%;width:70px;height:56px}
  .badge.tri{background:none;width:0;height:0;border-left:22px solid transparent;border-right:22px solid transparent;border-bottom:38px solid #c9c9c9}

  .footer{left:0;top:1096px;width:858px;height:104px;background:var(--slate);border-top:1px solid #ddd;text-align:center}
  .footer nav{display:flex;gap:24px;justify-content:center;margin-top:22px;font-size:11.5px}
  .footer nav a{color:var(--white);text-decoration:none}
  .footer small{display:block;font-size:10px;color:#a8abb0;line-height:12px}
  .footer small:first-of-type{margin-top:16px}
</style>
</head>
<body>
<div class="page">
  <div class="brand"><span class="brand-mark"></span><span class="brand-name">Varnet</span></div>

  <div class="social" aria-label="Social links"><span></span><span></span><span></span><span></span></div>

  <nav class="main-nav">
    <a class="current" href="#">Home</a><a href="#">Auctions</a><a href="#">Appraisals</a><a href="#">Real Estate</a><a href="#">FAQ</a><a href="#">About Us</a><a href="#">Contact Us</a>
  </nav>

  <section class="hero" role="img" aria-label="Wooden auction gavel resting on a desk beside stacked papers">
    <div class="hero-copy">
      <h1>THE BEST AUCTIONEERS<br>SINCE 1834</h1>
      <p>Lorem ipsum dolor sit amet, consectetur adipisicing elit, sed do eiusmod tempor incididunt ut labore et dolore m agna aliqua. Ut enim ad minim veniam <b>Read More....</b></p>
    </div>
    <div class="dots"><i></i><i></i><i></i><i></i><i></i></div>
  </section>

  <article class="card c1">
    <div class="photo" role="img" aria-label="Row of tagged wooden cabinets in a warehouse" style="background:linear-gradient(90deg,#b98a5c,#6e2a1e 45%,#5a1d17 75%,#b8a48a)"></div>
    <p>Lorem ipsum dolor sit amet, consectetur adipisicing elit, sed do eiusmod tempor incididunt <a href="#">Read More</a></p>
  </article>
  <article class="card c2">
    <div class="photo" role="img" aria-label="Vanity cabinets with granite tops and sinks" style="background:linear-gradient(#b9a99a,#4a3a32 35%,#a3602c 60%,#b57838)"></div>
    <p>Lorem ipsum dolor sit amet, consectetur adipisicing elit, sed do eiusmod tempor incididunt <a href="#">Read More</a></p>
  </article>
  <article class="card c3">
    <div class="photo" role="img" aria-label="Stacked rolls of carpet with yellow tags" style="background:linear-gradient(120deg,#8d7d62,#a8a396 40%,#6f7b80 70%,#8e8a82)"></div>
    <p>Lorem ipsum dolor sit amet, consectetur adipisicing elit, sed do eiusmod tempor incididunt <a href="#">Read More</a></p>
  </article>
  <article class="card c4">
    <div class="photo" role="img" aria-label="Row of white paneled doors with glass windows" style="background:linear-gradient(90deg,#c08b45,#dfe6ea 25%,#e9eef0 60%,#c79a5a)"></div>
    <p>Lorem ipsum dolor sit amet, consectetur adipisicing elit, sed do eiusmod tempor incididunt <a href="#">Read More</a></p>
  </article>

  <section class="subscribe">
    <h2>I want to know more about such items!</h2>
    <p>Subscribe and never miss out on finds &amp; deals delivered to your inbox.<br>(enter your email address below)</p>
    <div class="form"><div class="field">Enter your email</div><div class="btn">Subscribe Me</div></div>
  </section>

  <section class="partners" aria-label="Affiliations">
    <span class="arrow"><svg width="7" height="8" viewBox="0 0 7 8"><path d="M5 0L0 4l5 4z" fill="#fff"/></svg></span>
    <span class="badge"></span>
    <span class="badge round"></span>
    <span class="badge round" style="width:56px"></span>
    <span class="badge tri"></span>
    <span class="badge" style="width:50px"></span>
    <span class="badge round" style="width:78px"></span>
    <span class="arrow"><svg width="7" height="8" viewBox="0 0 7 8"><path d="M2 0l5 4-5 4z" fill="#fff"/></svg></span>
  </section>

  <footer class="footer">
    <nav><a href="#">Home</a><a href="#">Auctions</a><a href="#">Appraisals</a><a href="#">Real Estate</a><a href="#">FAQ</a><a href="#">About Us</a><a href="#">Contact Us</a></nav>
    <small>COPYRIGHT 2013. ALL RIGHTS RESERVED.</small>
    <small>TERMS &amp; CONDITIONS &nbsp;- &nbsp;PRIVACY &nbsp;- &nbsp;DISCLAIMER</small>
  </footer>
</div>
</body>
</html>
```